PRODUCT Catalog Design Project,Scope-4pages+1 Cover page,Click -http://fldr.xz/K8pwRt

Dear Friends ,
[ FERNO BOX LINK TO DOWNLOAD ALL CONTENT Photos & reference catalog - http://fldr.xz/K8pwRt
We would like to introduce ZORVANE GROUP PVT. LTD, we are into bulk material handling product which normally used in CEMENT,STEEL,PHARMA,FOOD Industry, We are looking for a catalog which should be attractive with lots pictures[ According to your design skills ] , FOR .PSD GOOD QUALITY IMAGES PLEASE SENT ME TEST MAIL ON RAHUL.PANTE@ZORVANEGROUP.COM ]
For further information please visit www.zorvanegroup.com

WHAT I WANT FROM YOU: please refer to ferno box link -http://fldr.xz/K8pwRt , i have enclosed some reference catalog picture for understanding color scheme and fonts
There are actual seven pages not properly arranged please find enclosed
First page : it should have very attractive look with product pictures for that i am enclosing each pictures please find enclosed and for description please find word file in which i have arranged data in front of respective picture
Enclosed
1- logo[ If you want to make small changes in logo according to catalog its fine ]
2- word 2010 file in which you will get description with pictures
3- cropped pictures [ if you want .psd format let me know i will provide that if you send me test mail on rahup

now important thing PLEASE SELECT THIS PROJECT only IF YOU REALLY HAVE EXPERIENCE IN INDUSTRIAL CATALOGUE WORK IN PAST
i want very interesting and such catalogue which meets industrial look requirement
Guys i am waiting for best design from you thank you very much for reading HAPPY NEW YEAR

hello every one,

I assure you that we will be give you extra amount of money , if our management team likes your design , we are new to tally hive we are not sure about its working .. 

please visit our website for more further information and description of our product  www.zorvanegroup.com

Reason: We haven't received any new attractive design yet , And we are really hopeful to receive from creative designer

For any photoshop format [.psd ] please send me mail on rahul.pante@zorvanegroup.com , since upload limit is only 30 mb i was not upload it ..Feel free to ask any questions

Thank you 

Reason: we are waiting for best creative design

Dear friends Now this project is committed , since we  are new to tally hive it was not committed but due request from some designers we are doing it right away, we have trust in you ....

Dear friends ,
For all documents, good quality pictures and REFERENCE CATALOG please click on ferno box link below,
These reference catalog just to understand what exactly we are expecting not exactly ,
Fonts -i love tavro products you can used any of font like Lucida Grande, myrid pro , and ya refer to reference for better understanding

FERNO BOX LINK -CLICK  -   http://fldr.xz/K8pwRt

Reason: designs are not as per our expectations.

FONTS -you can use MYRIAD PRO [ tavro product  fonts ] it looks attractive 

Target Market(s)

People who are engineers , managing directors, purchase department managers ..
age group 24 - 65

Industry/Entity Type

Industrial

Requirements
Must have
• ELEGANT COLORS, PLEASE DO NOT USE GOODY COLORS
Nice to have
• colorful lots of shapes please see ferno box link click on that download reference catalog http://fldr.xz/K8pwRt

```html
<!DOCTYPE html>
<html lang="en">
<head>
<meta charset="utf-8">
<title>Rotary Air Lock Valves — Catalog Spread</title>
<link href="https://fonts.googleapis.com/css2?family=Source+Sans+3:wght@400;600&display=swap" rel="stylesheet">
<style>
:root{
  --bg:#ffffff;
  --paper:#ffffff;
  --ink:#6b7378;
  --ink-dark:#4f575c;
  --slate:#6f787d;
  --lavender:#e4d5e8;
  --lavender-soft:#f5f3f7;
  --sand:#e8cf94;
  --sand-soft:#fbf7ee;
  --rule:#9aa0a4;
}
*{margin:0;padding:0;box-sizing:border-box}
html,body{width:1200px;height:848px;overflow:hidden;background:var(--bg)}
body{font-family:"Source Sans 3",sans-serif;color:var(--ink);position:relative}
.spread{position:absolute;left:135px;top:86px;width:930px;height:659px;background:var(--paper)}
.shapes{position:absolute;left:0;top:0}
.abs{position:absolute}
.page-title{font-size:27px;font-weight:400;color:var(--ink);line-height:1;top:40px}
.page-title.left{left:37px}
.page-title.right{right:41px}
.tab-label{font-size:14px;color:#fff;top:89px;letter-spacing:.3px}
.tab-label.left{left:37px}
.tab-label.right{right:41px}
.intro{font-size:9.8px;line-height:12.6px;width:376px;top:131px}
.intro p{margin-bottom:5px}
.intro.left{left:40px}
.intro.right{left:505px;width:380px}
.intro ul{list-style:none}
.intro li{position:relative;padding-left:10px;margin-bottom:5px}
.intro li::before{content:"";position:absolute;left:0;top:5px;width:4px;height:4px;border-radius:50%;background:var(--ink)}
.product-photo{float:right;border-radius:4px}
.photo-left{width:175px;height:98px;margin:0 0 6px 10px;background:linear-gradient(135deg,#8a8c86,#c9c8c2 55%,#5d5f5b)}
.photo-right{width:182px;height:100px;margin:2px 0 30px 12px;background:linear-gradient(135deg,#4a78b8,#b9bcc0 45%,#7d8084)}
.size-table{width:80px;top:336px;font-size:8.5px;text-align:center}
.size-table .head{background:var(--slate);color:#fff;font-weight:600;height:18px;line-height:18px;font-size:8px}
.size-table .body{background:var(--lavender);padding:12px 0 2px;line-height:9.7px}
.spec-box{top:446px;width:386px;height:173px;padding:12px 10px 0 10px;display:flex;gap:14px}
.spec-box.left{left:40px;background:var(--lavender-soft)}
.spec-box.right{left:505px;background:var(--sand-soft)}
.col{width:176px;font-size:7.4px;line-height:9.6px}
.col h3{font-size:9px;font-weight:400;color:var(--ink-dark);letter-spacing:.5px;margin-bottom:3px}
.col ul{list-style:none;margin-bottom:4px}
.col li{position:relative;padding-left:10px;margin-bottom:2.4px}
.col li::before{content:"";position:absolute;left:1px;top:3.6px;width:3px;height:3px;border-radius:50%;background:var(--ink)}
.col hr{border:0;border-top:1px solid var(--rule);margin:3px 0 7px}
.folio{font-size:7px;top:638px}
.folio.left{left:15px}
.folio.right{right:20px}
</style>
</head>
<body>
<div class="spread">
  <svg class="shapes" width="930" height="659" viewBox="0 0 930 659" aria-hidden="true">
    <polygon points="0,26 425,26 425,82 370,82 355,97 125,97 110,82 0,82" fill="var(--lavender)"/>
    <polygon points="0,82 126,82 141,96.5 126,111 0,111" fill="var(--slate)"/>
    <polygon points="505,26 930,26 930,82 810,82 795,97 580,97 565,82 505,82" fill="var(--sand)"/>
    <polygon points="930,82 805,82 790,96.5 805,111 930,111" fill="var(--slate)"/>
  </svg>

  <h1 class="abs page-title left">Side Entry Side Discharge Type</h1>
  <div class="abs tab-label left">OSD-ZRV</div>

  <div class="abs intro left">
    <p>Side Entry – Side discharge model Rotary Air Lock Valve lines are specially designed with offset inlet and discharge opening to reduce product shearing while maintaining an efficient product flow in conveying or metering applications.</p>
    <p>The Valve name derives form the Offset inlet and outlet flanges, where product enters the side of the rotor instead of top.</p>
    <div class="product-photo photo-left" role="img" aria-label="Photo of side entry side discharge rotary air lock valve with motor"></div>
    <p>On a normal valve, shearing takes place as rotor rotates into the housing. When these two edges meet on a typical drop thru rotary Air Lock the product is caught on the upswing of the rotor blades so that the product is constantly filling away from the shear point. The rotor pockets also do not fill completely, reducing the likehood of shearing. Lastly, the through out has V shape which helps push product out of the way.</p>
  </div>

  <div class="abs size-table" style="left:40px">
    <div class="head">Circular Flange</div>
    <div class="body">150<br>200<br>250<br>300<br>350<br>400<br>500</div>
  </div>
  <div class="abs size-table" style="left:127px">
    <div class="head">Square Flange</div>
    <div class="body">150<br>200<br>250<br>300<br>350<br>400<br>500</div>
  </div>

  <section class="abs spec-box left">
    <div class="col">
      <h3>CORE UNMATCHED FEATURES</h3>
      <ul>
        <li>Available in sized 150mm to 1000mm</li>
        <li>Maintenance free</li>
        <li>Offset side inlet and discharge provides optimal material product flow</li>
        <li>Round Flange</li>
        <li>Optimal adjustable slide gate for optimal material feed, rate control</li>
        <li>"V" type inlet throat minimizes product shearing and degradation</li>
        <li>Housing vent connection improves valve efficiency</li>
        <li>Rugged corrosion resistant cast stainless steel construction provides maximum structural stability</li>
      </ul>
    </div>
    <div class="col" style="margin-top:-3px">
      <ul>
        <li>Out board sealed bearings never need lubrication</li>
        <li>8-Vane open end rotor standard for optimal air seal and product feed</li>
      </ul>
      <hr>
      <h3>COMMON SERVICE CONDITIONS</h3>
      <ul>
        <li>Pressure Rating: 15 PSI.</li>
        <li>Maximum Operating Temperature: 1000 C</li>
        <li>Materials: Pellets, Chips, Flakes, Cubes.</li>
      </ul>
      <hr>
      <h3>TYPICAL APPLICATIONS</h3>
      <ul>
        <li>Railcar unloading</li>
        <li>Pneumatic Conveying</li>
        <li>Vacuum Loaders</li>
      </ul>
    </div>
  </section>

  <h1 class="abs page-title right">Rapid Rinse Series</h1>
  <div class="abs tab-label right">RR-ZRV</div>

  <div class="abs intro right">
    <p>The Rapid Rinse Series is designed for fast disassembly, cleaning and reassembly of the material contact surface. The Rapid Rinse is specifically designed to be cleaned without tools and removal from service. This type of valve we normally supply to the pharmaceutical industry and food industry.</p>
    <div class="product-photo photo-right" role="img" aria-label="Photo of quick-cleaning rotary valve with blue motor"></div>
    <ul>
      <li>The Rapid Rinse Rotary Valves are specially designed for application where frequent cleaning, sanitizing or inspection of the bulk handling system is required with minimum down time. They are also ideal for batch systems where regular cleaning between cycles is required.</li>
      <li>The valve needs no tools to unscrew the release handles and remove the head plate. Four slide bars with linear bearings, provide maximum support for the rotor. The rotor and head plate can be pulled out and the valve can be thoroughly cleaned, sanitized and inspected.</li>
      <li>Re-assembly is quick and simplified as no special tools are required.</li>
      <li>Three design levels to meet your specific cleaning needs in stainless or polished sanitary.</li>
    </ul>
  </div>

  <section class="abs spec-box right">
    <div class="col">
      <h3>CORE COMPETITIVE ADVANTAGES</h3>
      <ul>
        <li>Available in 3 sizes from through 200 X 300m</li>
        <li>SS 316 and 304 are standard providing maximum structural stability</li>
        <li>Tool-free hand fasteners for rotor removal and regular inspections</li>
        <li>Four Slide bar design, using linear, bearings for full support of rotor and head plate</li>
        <li>Permanently Sealed bearings ensure protection for contamination</li>
      </ul>
    </div>
    <div class="col">
      <h3>GENERAL SERVICE CONDITION</h3>
      <ul>
        <li>Pressure Ration: 15 psi</li>
        <li>Maximum Operating Temperature: 400°F</li>
        <li>Materials: Dry Free-Flowing Food grad or contamination sensitive Powders</li>
      </ul>
      <hr>
      <h3>TYPICAL APPLICATIONS</h3>
      <ul>
        <li>Pneumatic Conveying</li>
        <li>Blending</li>
        <li>Dust collection Drying Weighing Mixing</li>
      </ul>
    </div>
  </section>

  <div class="abs folio left">06</div>
  <div class="abs folio right">07</div>
</div>
</body>
</html>
```